Brisk Laundromat Brochure for student plans

Im in need of a .trifold brochure ASAP I have attached a powerpoint presentation as well as my logo. I would like a page describing Student subscription plans another page describing non monthly plans while using graphics provided

Target Market(s)

College Students

Industry/Entity Type

Laundromat

Font styles to use
Serif
Sans Serif
Other font styles liked:
• Use font from laundromat logo

Colors
EE7325
F08F49
F5BC92
FAE3D3
FDF4ED

Requirements
Must have
• Must have student plans and logo design on the Brochure
Nice to have
• The college of westbrook logo and photos that can be found within the power point presantation
Should not have
• Should not have stock photos try to use photos provided

```html
<!DOCTYPE html>
<html lang="en">
<head>
<meta charset="utf-8">
<title>Brisk Laundromat – Student Plans Trifold</title>
<link href="https://fonts.googleapis.com/css2?family=Bebas+Neue&family=Hind:wght@400;500;600;700&family=Montserrat:wght@500;600;800&display=swap" rel="stylesheet">
<style>
  :root{
    --orange:#EE7325;
    --orange-soft:#F08F49;
    --blue:#3E54A8;
    --cyan:#29A8E0;
    --ink:#1d1d1f;
    --paper:#ffffff;
    --backdrop:#e9e6e1;
  }
  *{box-sizing:border-box;margin:0;padding:0}
  html,body{width:1200px;height:1200px;overflow:hidden;background:var(--backdrop)}
  .canvas{position:relative;width:1200px;height:1200px;overflow:hidden}
  .sheet{position:absolute;left:240px;width:720px;height:554px;background:var(--paper);overflow:hidden;box-shadow:0 2px 10px rgba(0,0,0,.18)}
  .sheet--outside{top:31px}
  .sheet--inside{top:615px}
  .sheet svg.shapes{position:absolute;inset:0}
  .abs{position:absolute}
  .display{font-family:"Bebas Neue",sans-serif;letter-spacing:.5px;line-height:.95}
  .wordmark{font-family:"Montserrat",sans-serif;font-weight:800;line-height:1;text-align:center}
  .wordmark .name{display:block}
  .wordmark .tag{display:block;font-weight:500;letter-spacing:5px}

  /* outside: about */
  .about{left:26px;top:196px;width:190px;color:#fff;font-family:"Montserrat",sans-serif}
  .about h2{font-size:15px;font-weight:800;margin-bottom:10px}
  .about p{font-size:9.6px;font-weight:500;line-height:1.33;letter-spacing:.3px;text-align:justify;margin-bottom:11px}

  /* outside: app */
  .phone{left:272px;top:26px;width:74px;height:152px;border:3px solid #111;border-radius:12px;background:#fff}
  .phone .wordmark{position:absolute;left:0;right:0;top:60px;color:var(--blue)}
  .phone .name{font-size:17px}
  .phone .tag{font-size:4px;letter-spacing:1.6px;color:var(--orange)}
  .app-promo{left:358px;top:24px}
  .app-promo .kicker{font-family:"Hind",sans-serif;font-weight:700;color:var(--orange);font-size:10px}
  .app-promo .title{color:var(--cyan);font-size:19.5px;margin-top:2px}
  .store-badge{position:absolute;left:358px;width:65px;height:19px;background:#111;border-radius:3px}

  /* outside: contact */
  .contact{left:272px;top:198px;color:#fff}
  .contact h2{font-family:"Montserrat",sans-serif;font-weight:800;font-size:15px;margin-bottom:8px}
  .contact ul{list-style:none;font-family:"Hind",sans-serif;font-size:10.2px;line-height:1.25}
  .contact li{display:flex;gap:5px;margin-bottom:5px}
  .contact svg{flex:none;margin-top:1px}
  .contact-mark{left:272px;top:318px;width:120px;color:#fff}
  .contact-mark .name{font-size:42px}
  .contact-mark .tag{font-size:8px;margin-top:2px}
  .follow{left:240px;top:400px;width:192px;height:30px;background:var(--cyan);display:flex;align-items:center;padding-left:26px;gap:5px;color:#fff;font-family:"Montserrat",sans-serif;font-weight:800;font-size:11px}
  .follow i{display:inline-block;width:12px;height:12px;border-radius:50%;background:#fff}
  .follow span{margin-right:4px}

  /* outside: cover */
  .cover-mark{left:496px;top:20px;width:210px;color:var(--blue)}
  .cover-mark .name{font-size:56px}
  .cover-mark .tag{font-size:11px;color:var(--orange);letter-spacing:7px;margin-top:4px}
  .cover-title{left:504px;top:452px;color:#fff;font-size:38px;white-space:nowrap}
  .cover-url{left:503px;top:524px;color:#fff;font-family:"Hind",sans-serif;font-weight:500;font-size:12px}

  /* inside: services */
  .services-head{left:26px;top:353px;font-family:"Hind",sans-serif;font-weight:700;font-size:13.5px;line-height:1.15}
  .services-head .a{color:var(--cyan)}
  .services-head .b{color:var(--orange)}
  .service{position:absolute;left:27px;display:flex;gap:10px;align-items:center;color:#fff;font-family:"Hind",sans-serif}
  .service .badge{width:46px;height:46px;border-radius:50%;background:#fff;border:4px solid var(--cyan);display:flex;align-items:center;justify-content:center;flex:none}
  .service h3{color:var(--cyan);font-size:11px;font-weight:600;line-height:1.1}
  .service p{font-size:9.5px;line-height:1.2}

  /* inside: plans */
  .plans{left:266px;top:24px;width:190px;font-family:"Hind",sans-serif;color:var(--ink)}
  .plans h2,.alt h2{color:var(--orange);font-size:12.5px;font-weight:600;line-height:1.2;margin-bottom:6px}
  .plans .lead,.alt .lead{font-weight:600;font-size:9.4px;line-height:1.25;margin-bottom:4px}
  .plans ul{list-style:none;font-size:9.3px;line-height:1.25}
  .plans li{position:relative;padding-left:11px;margin-bottom:4.5px}
  .plans li::before{content:"";position:absolute;left:0;top:2.5px;width:7px;height:7px;border-radius:50%;background:var(--cyan)}
  .perks{position:absolute;left:263px;top:198px;width:196px;display:flex;justify-content:space-between;font-family:"Hind",sans-serif;font-size:8.6px;line-height:1.15;text-align:center;color:var(--ink)}
  .perk{width:64px;display:flex;flex-direction:column;align-items:center;gap:4px}
  .perk + .perk{border-left:1px dashed var(--orange)}
  .perk .dot{width:25px;height:25px;border-radius:50%;background:var(--blue)}
  .perks-note{left:266px;top:259px;font-family:"Hind",sans-serif;font-size:9.5px;color:var(--ink)}

  .alt{left:505px;top:24px;width:200px;font-family:"Hind",sans-serif;color:var(--ink)}
  .bag-label{position:absolute;background:var(--cyan);color:#fff;font-family:"Hind",sans-serif;font-weight:700;font-size:10.5px;height:14px;line-height:15px;padding-left:5px}
  .bag-copy{position:absolute;font-family:"Hind",sans-serif;font-size:8.5px;line-height:1.25;color:var(--ink)}
  .mini-perk{position:absolute;display:flex;gap:5px;align-items:center;font-family:"Hind",sans-serif;font-size:8.6px;line-height:1.1;color:var(--ink)}
  .mini-perk .dot{width:24px;height:24px;border-radius:50%;background:var(--blue);border:2px solid #cfd6ee}
  .inside-mark{left:365px;top:484px;width:92px;color:#fff}
  .inside-mark .name{font-size:32px}
  .inside-mark .tag{font-size:6px;letter-spacing:3px;margin-top:1px}
</style>
</head>
<body>
<main class="canvas">

  <!-- OUTSIDE -->
  <section class="sheet sheet--outside" aria-label="Brochure outside">
    <svg class="shapes" width="720" height="554" viewBox="0 0 720 554">
      <g role="img" aria-label="Photo of stacked washers above a checkered laundromat floor">
        <rect x="0" y="0" width="240" height="184" fill="url(#gWashers)"/>
      </g>
      <rect x="0" y="184" width="240" height="216" fill="var(--orange)"/>
      <g role="img" aria-label="Photo of the two owners in orange shirts in front of dryers">
        <rect x="0" y="400" width="240" height="154" fill="url(#gOwners)"/>
      </g>
      <rect x="240" y="184" width="240" height="216" fill="var(--blue)"/>
      <rect x="470" y="116" width="250" height="324" fill="var(--blue)"/>
      <g role="img" aria-label="Photo of a smiling attendant in a yellow apron holding a laundry basket">
        <polygon points="468,116 720,116 720,380 700,430 440,430 440,300 460,184" fill="url(#gWoman)"/>
      </g>
      <g role="img" aria-label="Photo of a row of front-loading washers">
        <polygon points="240,430 462,430 432,554 240,554" fill="url(#gRow)"/>
      </g>
      <polygon points="462,430 720,380 720,554 432,554" fill="var(--orange)"/>
      <polygon points="470,434 706,434 686,514 448,514" fill="var(--blue)"/>
      <polygon points="448,514 462,514 442,554 430,554" fill="var(--blue)"/>
      <circle cx="704" cy="462" r="2" fill="#fff"/>
      <circle cx="707" cy="487" r="2.5" fill="#fff"/>
      <circle cx="697" cy="513" r="5" fill="#fff"/>
      <circle cx="711" cy="520" r="4" fill="#fff"/>
      <circle cx="692" cy="527" r="6" fill="#fff"/>
      <defs>
        <linearGradient id="gWashers" x1="0" y1="0" x2="0" y2="1"><stop offset="0" stop-color="#c9ccd2"/><stop offset=".7" stop-color="#8a8e96"/><stop offset="1" stop-color="#3a3c42"/></linearGradient>
        <linearGradient id="gOwners" x1="0" y1="0" x2="1" y2="1"><stop offset="0" stop-color="#b8bcc3"/><stop offset=".5" stop-color="#ec7a37"/><stop offset="1" stop-color="#7f6a64"/></linearGradient>
        <linearGradient id="gWoman" x1="0" y1="0" x2="0" y2="1"><stop offset="0" stop-color="#c3c8cf"/><stop offset=".55" stop-color="#e8b54a"/><stop offset="1" stop-color="#3b3d44"/></linearGradient>
        <linearGradient id="gRow" x1="0" y1="0" x2="1" y2="0"><stop offset="0" stop-color="#f4f5f7"/><stop offset="1" stop-color="#9ea3ab"/></linearGradient>
      </defs>
    </svg>

    <div class="abs about">
      <h2>ABOUT US</h2>
      <p>Owen and Marcus are the owners of Brisk Laundromat, formally Rosalind's Coin Laundry.</p>
      <p>In 2023, Brisk has undergone major renovations and installation of new high efficiency washers and dryers.</p>
      <p>Come visit us today, and see how we're changing your laundromat experience.</p>
    </div>

    <div class="abs phone"><div class="wordmark"><span class="name">Brisk</span><span class="tag">LAUNDROMAT</span></div></div>
    <div class="abs app-promo">
      <div class="kicker">DON'T MISS IT!</div>
      <div class="display title">DOWLOAD OUR<br>PICKUP<br>/DELIVERY APP</div>
    </div>
    <div class="store-badge" style="top:119px"></div>
    <div class="store-badge" style="top:147px"></div>

    <div class="abs contact">
      <h2>CONTACT US</h2>
      <ul>
        <li><svg width="11" height="11" viewBox="0 0 12 12"><circle cx="6" cy="6" r="5.4" fill="none" stroke="#fff" stroke-width=".9"/><path d="M6 2.8a2 2 0 0 1 2 2c0 1.5-2 3.8-2 3.8S4 6.3 4 4.8a2 2 0 0 1 2-2z" fill="#fff"/></svg><span>48 Harbor Ln, Westbrook,<br>MA, United States, 01990</span></li>
        <li><svg width="11" height="11" viewBox="0 0 12 12"><circle cx="6" cy="6" r="5.4" fill="none" stroke="#fff" stroke-width=".9"/><path d="M4 3.2l1.1 1.4-.6.8c.4.9 1.1 1.6 2 2l.8-.6L8.8 8l-.8.9C5.6 8.6 3.4 6.4 3.1 4z" fill="#fff"/></svg><span>555-014-0264</span></li>
        <li><svg width="11" height="11" viewBox="0 0 12 12"><circle cx="6" cy="6" r="5.4" fill="none" stroke="#fff" stroke-width=".9"/><rect x="3.2" y="4" width="5.6" height="4" fill="none" stroke="#fff" stroke-width=".8"/><path d="M3.2 4L6 6.2 8.8 4" fill="none" stroke="#fff" stroke-width=".8"/></svg><span>hello@brisklaundromat.com</span></li>
        <li><svg width="11" height="11" viewBox="0 0 12 12"><circle cx="6" cy="6" r="5.4" fill="none" stroke="#fff" stroke-width=".9"/><circle cx="6" cy="6" r="3" fill="none" stroke="#fff" stroke-width=".8"/><path d="M3 6h6M6 3v6" stroke="#fff" stroke-width=".8"/></svg><span>www.brisklaundromat.com</span></li>
      </ul>
    </div>
    <div class="abs wordmark contact-mark"><span class="name">Brisk</span><span class="tag">LAUNDROMAT</span></div>
    <div class="follow"><span>FOLLOW US</span><i></i><i></i><i></i></div>

    <div class="abs wordmark cover-mark"><span class="name">Brisk</span><span class="tag">LAUNDROMAT</span></div>
    <div class="abs display cover-title">STUDENT PLANS</div>
    <div class="abs cover-url">www.brisklaundromat.com</div>
  </section>

  <!-- INSIDE -->
  <section class="sheet sheet--inside" aria-label="Brochure inside">
    <svg class="shapes" width="720" height="554" viewBox="0 0 720 554">
      <g role="img" aria-label="Photo of an owner carrying a large laundry bag beside red and blue drawstring bags">
        <polygon points="0,0 238,0 198,328 0,262" fill="url(#gBags)"/>
      </g>
      <polygon points="238,0 248,0 208,330 198,328" fill="var(--orange)"/>
      <polygon points="0,262 198,328 304,554 0,554" fill="var(--blue)"/>
      <g role="img" aria-label="Photo of stainless steel front-load washers">
        <polygon points="208,330 480,290 480,400 280,505" fill="url(#gMachines)"/>
      </g>
      <polygon points="280,505 480,400 720,340 720,554 304,554" fill="var(--orange)"/>
      <polygon points="280,505 480,400 480,406 283,511" fill="var(--cyan)"/>
      <polygon points="198,328 208,330 314,554 304,554" fill="var(--cyan)"/>
      <g role="img" aria-label="Photo of red and blue branded laundry bags">
        <rect x="506" y="336" width="196" height="212" rx="6" fill="url(#gBrand)"/>
      </g>
      <g role="img" aria-label="Photo of a small black laundry bag"><rect x="508" y="72" width="50" height="52" rx="5" fill="#26272b"/></g>
      <g role="img" aria-label="Photo of a blue laundry bag"><rect x="617" y="131" width="76" height="70" rx="5" fill="#2f63c9"/></g>
      <g role="img" aria-label="Photo of a red drawstring laundry bag"><rect x="504" y="196" width="56" height="96" rx="10" fill="#e23b3b"/></g>
      <circle cx="279" cy="538" r="5" fill="#fff"/>
      <circle cx="290" cy="530" r="4" fill="#fff"/>
      <circle cx="283" cy="522" r="3" fill="#fff"/>
      <circle cx="276" cy="508" r="2" fill="#fff"/>
      <defs>
        <linearGradient id="gBags" x1="0" y1="0" x2="1" y2="1"><stop offset="0" stop-color="#6f7a5c"/><stop offset=".45" stop-color="#d9405a"/><stop offset=".8" stop-color="#e2433b"/><stop offset="1" stop-color="#2f55b8"/></linearGradient>
        <linearGradient id="gMachines" x1="0" y1="0" x2="1" y2="0"><stop offset="0" stop-color="#9aa0a8"/><stop offset=".5" stop-color="#d3d6db"/><stop offset="1" stop-color="#a7acb4"/></linearGradient>
        <linearGradient id="gBrand" x1="0" y1="0" x2="1" y2="1"><stop offset="0" stop-color="#d9304d"/><stop offset=".55" stop-color="#e03a52"/><stop offset="1" stop-color="#2a5cc4"/></linearGradient>
      </defs>
    </svg>

    <div class="abs services-head"><div class="a">BRISK LAUNDROMAT</div><div class="b">OFFERS 3 SERVICES</div></div>
    <div class="service" style="top:392px">
      <div class="badge"><svg width="22" height="22" viewBox="0 0 22 22"><rect x="3" y="2" width="16" height="18" rx="2" fill="none" stroke="var(--blue)" stroke-width="1.5"/><circle cx="11" cy="12" r="4.5" fill="none" stroke="var(--blue)" stroke-width="1.5"/></svg></div>
      <div><h3>Coin Laundry</h3><p>Sizes ranging from 20 lb to<br>80 lb washers</p></div>
    </div>
    <div class="service" style="top:444px">
      <div class="badge"><svg width="22" height="22" viewBox="0 0 22 22"><path d="M11 3l-2 2-5 2v12h14V7l-5-2z" fill="none" stroke="var(--blue)" stroke-width="1.5"/><path d="M11 5v14" stroke="var(--blue)" stroke-width="1.2"/></svg></div>
      <div><h3>Wash Dry &amp; Fold</h3><p>Low prices starting at<br>$1.00</p></div>
    </div>
    <div class="service" style="top:496px">
      <div class="badge"><svg width="22" height="22" viewBox="0 0 22 22"><rect x="2" y="6" width="11" height="9" fill="none" stroke="var(--blue)" stroke-width="1.5"/><path d="M13 9h4l3 3v3h-7z" fill="none" stroke="var(--blue)" stroke-width="1.5"/><circle cx="6" cy="17" r="1.8" fill="var(--blue)"/><circle cx="16" cy="17" r="1.8" fill="var(--blue)"/></svg></div>
      <div><h3>Free Delivery</h3><p>App and Web enabled.<br>Servicing all of South Coast.</p></div>
    </div>

    <div class="abs plans">
      <h2>And now, cost effective Student &amp; Faculty Subscription Plans</h2>
      <p class="lead">Student &amp; Faculty will select the size that meets their needs:</p>
      <ul>
        <li>Standard Bag, up to 40 pounds of laundry, $119/mo ($0.75/lb)</li>
        <li>Large Bag, up to 60 pounds of laundry, $139/mo ($0.59/lb)</li>
        <li>Monthly Subscription Plan required.</li>
        <li>1 bag per week.</li>
        <li>Cancel anytime.</li>
      </ul>
    </div>
    <div class="perks">
      <div class="perk"><span class="dot"></span>Convenient<br>&amp; Hassle Free</div>
      <div class="perk"><span class="dot"></span>App &amp;<br>Web Enabled</div>
      <div class="perk"><span class="dot"></span>Free<br>Delivery</div>
    </div>
    <div class="abs perks-note">All this, for just cents per pound of laundry!</div>

    <div class="abs alt">
      <h2>Or as an alternate, Free Delivery Plans are also Available</h2>
      <p class="lead">Select the size that meets your needs:</p>
    </div>
    <div class="bag-label" style="left:565px;top:78px;width:140px">Small Black Bag: $25</div>
    <div class="bag-copy" style="left:565px;top:96px">Small Bag, up to 20 pounds<br>of laundry, $25 / bag</div>
    <div class="bag-label" style="left:505px;top:139px;width:110px">Standard Bag: $50</div>
    <div class="bag-copy" style="left:505px;top:156px">Standard Bag, up to<br>40 pounds of laundry,<br>$50 / bag</div>
    <div class="bag-label" style="left:565px;top:223px;width:140px">X-Large Bag: $75</div>
    <div class="bag-copy" style="left:565px;top:240px">Large Bag, up to<br>60 pounds of laundry,<br>$75 /bag</div>
    <div class="mini-perk" style="left:506px;top:300px"><span class="dot"></span>App &amp; Web<br>Enabled</div>
    <div class="mini-perk" style="left:596px;top:300px"><span class="dot"></span>Free<br>Delivery</div>

    <div class="abs wordmark inside-mark"><span class="name">Brisk</span><span class="tag">LAUNDROMAT</span></div>
  </section>

</main>
</body>
</html>
```